We have a new logo so we need to change our business card

We're super Happy with our current cards but I think with a new logo should come a new design. I wouldn't mind seeing the icons that we used on the back last time reused on this card. Please feel free to visit our website to get a sense for our brand www.brindlewick.ca

I need the final final to have contact info for:

Gordon Hasley
Co-Owner
info@brindlewick.ca
778-315-6207

and

Marjorie Hasley
Co-Owner
info@brindlewick.ca
778-342-5810

Target Market(s)

Female dog owners, 21 to 70

Industry/Entity Type

pet industry

Contact Information for Business Card

included in brief

Requirements
Should not have
• We do not want it to look cartonish

```html
<!DOCTYPE html>
<html lang="en">
<head>
<meta charset="utf-8">
<title>Brindlewick Business Card</title>
<link href="https://fonts.googleapis.com/css2?family=Montserrat:wght@400;500;700;800&display=swap" rel="stylesheet">
<style>
  :root {
    --ink: #1f1d22;
    --green: #7cc243;
    --white: #ffffff;
    --paper: #dcdcdc;
    --badge: #6b6f70;
    --badge-rim: #b9bcbc;
    --badge-light: #e6e7e7;
    --badge-light-rim: #9a9d9d;
    --text-dark: #222222;
  }
  * { box-sizing: border-box; margin: 0; padding: 0; }
  html, body { width: 1200px; height: 800px; overflow: hidden; }
  body {
    background: var(--paper);
    font-family: "Montserrat", sans-serif;
    position: relative;
  }
  .card {
    position: absolute;
    left: 290px;
    width: 620px;
    height: 354px;
    border-radius: 22px;
    overflow: hidden;
    box-shadow: 0 6px 18px rgba(0,0,0,0.18);
  }
  .card--front { top: 30px; background: var(--white); }
  .card--back { top: 414px; background: var(--ink); }

  .front-bg { position: absolute; inset: 0; width: 100%; height: 100%; }

  .brand {
    position: absolute;
    top: 36px;
    right: 52px;
    display: flex;
    align-items: center;
    gap: 14px;
  }
  .brand-dot {
    width: 56px; height: 56px;
    border-radius: 50%;
    background: var(--green);
  }
  .brand-name {
    color: var(--white);
    font-weight: 700;
    font-size: 42px;
    letter-spacing: -0.5px;
  }

  .contact {
    position: absolute;
    left: 44px;
    top: 206px;
  }
  .contact-name {
    color: var(--green);
    font-weight: 800;
    font-size: 25px;
    line-height: 1.1;
    letter-spacing: 0.5px;
    text-transform: uppercase;
  }
  .contact-role {
    color: var(--text-dark);
    font-size: 15px;
    margin-top: 2px;
  }
  .contact-rule {
    width: 44px; height: 3px;
    background: var(--green);
    margin: 8px 0 8px;
  }
  .contact-line {
    display: flex;
    align-items: center;
    gap: 10px;
    color: var(--text-dark);
    font-size: 16px;
    line-height: 1.5;
  }
  .contact-line svg { width: 14px; height: 14px; fill: var(--green); flex: none; }

  .web-pill {
    position: absolute;
    right: 40px;
    bottom: 60px;
    background: var(--green);
    color: var(--text-dark);
    border-radius: 18px;
    padding: 7px 18px;
    font-size: 14px;
  }
  .web-pill strong { font-weight: 700; }

  .benefits {
    position: absolute;
    left: 40px;
    top: 50px;
    width: 330px;
  }
  .benefits-tag {
    display: inline-block;
    background: var(--green);
    color: var(--ink);
    font-weight: 800;
    font-size: 17px;
    border-radius: 14px;
    padding: 4px 14px;
    letter-spacing: 0.5px;
    margin-bottom: 12px;
  }
  .benefit-list { list-style: none; }
  .benefit-item {
    display: flex;
    gap: 10px;
    color: var(--white);
    font-size: 13.5px;
    line-height: 1.45;
    margin-bottom: 4px;
  }
  .benefit-tick {
    flex: none;
    width: 15px; height: 15px;
    margin-top: 2px;
    border-radius: 50%;
    background: var(--green);
    display: flex; align-items: center; justify-content: center;
  }
  .benefit-tick svg { width: 9px; height: 9px; }

  .badges {
    position: absolute;
    right: 40px;
    top: 70px;
    display: grid;
    grid-template-columns: repeat(2, 76px);
    gap: 18px 26px;
  }
  .badge {
    width: 76px; height: 76px;
    border-radius: 50%;
    background: var(--badge);
    border: 4px solid var(--badge-rim);
  }
  .badge--light { background: var(--badge-light); border-color: var(--badge-light-rim); }
</style>
</head>
<body>

  <section class="card card--front" aria-label="Business card front">
    <svg class="front-bg" viewBox="0 0 620 354" preserveAspectRatio="none" aria-hidden="true">
      <path d="M0 0 H620 V104 C585 150 520 160 420 162 C300 165 120 150 0 178 Z" fill="var(--ink)"/>
      <path d="M0 178 C120 150 300 165 420 162 C520 160 585 150 620 104 V120 C585 166 520 174 420 176 C300 179 120 166 0 192 Z" fill="var(--green)"/>
    </svg>

    <div class="brand">
      <span class="brand-dot"></span>
      <span class="brand-name">Brindlewick</span>
    </div>

    <div class="contact">
      <p class="contact-name">Gordon Hasley</p>
      <p class="contact-role">Co-Owner</p>
      <div class="contact-rule"></div>
      <p class="contact-line">
        <svg viewBox="0 0 24 24"><path d="M6.6 10.8a15.1 15.1 0 0 0 6.6 6.6l2.2-2.2a1 1 0 0 1 1-.25 11.4 11.4 0 0 0 3.6.57 1 1 0 0 1 1 1V20a1 1 0 0 1-1 1A17 17 0 0 1 3 4a1 1 0 0 1 1-1h3.5a1 1 0 0 1 1 1c0 1.25.2 2.45.57 3.57a1 1 0 0 1-.25 1z"/></svg>
        778-315-6207
      </p>
      <p class="contact-line">
        <svg viewBox="0 0 24 24"><path d="M2 5h20v14H2z M4 7v.5l8 5 8-5V7l-8 5z" fill-rule="evenodd"/></svg>
        info@brindlewick.ca
      </p>
    </div>

    <p class="web-pill">www.<strong>brindlewick</strong>.ca</p>
  </section>

  <section class="card card--back" aria-label="Business card back">
    <div class="benefits">
      <span class="benefits-tag">BENEFITS</span>
      <ul class="benefit-list">
        <li class="benefit-item"><span class="benefit-tick"><svg viewBox="0 0 10 10"><path d="M1.5 5.2l2.2 2.2 4.8-4.8" stroke="#1f1d22" stroke-width="1.8" fill="none"/></svg></span>Improves condition of the skin and fur</li>
        <li class="benefit-item"><span class="benefit-tick"><svg viewBox="0 0 10 10"><path d="M1.5 5.2l2.2 2.2 4.8-4.8" stroke="#1f1d22" stroke-width="1.8" fill="none"/></svg></span>Reduces shedding and dandruff</li>
        <li class="benefit-item"><span class="benefit-tick"><svg viewBox="0 0 10 10"><path d="M1.5 5.2l2.2 2.2 4.8-4.8" stroke="#1f1d22" stroke-width="1.8" fill="none"/></svg></span>Strengthens the immune system</li>
        <li class="benefit-item"><span class="benefit-tick"><svg viewBox="0 0 10 10"><path d="M1.5 5.2l2.2 2.2 4.8-4.8" stroke="#1f1d22" stroke-width="1.8" fill="none"/></svg></span>Helps eliminate unwanted odours</li>
        <li class="benefit-item"><span class="benefit-tick"><svg viewBox="0 0 10 10"><path d="M1.5 5.2l2.2 2.2 4.8-4.8" stroke="#1f1d22" stroke-width="1.8" fill="none"/></svg></span>Adds a scented benefit</li>
        <li class="benefit-item"><span class="benefit-tick"><svg viewBox="0 0 10 10"><path d="M1.5 5.2l2.2 2.2 4.8-4.8" stroke="#1f1d22" stroke-width="1.8" fill="none"/></svg></span>Helps with; anxiety, arthritis, insomnia drowsiness, skin irritation &amp; depression</li>
      </ul>
    </div>

    <div class="badges" aria-label="Product certification badges">
      <span class="badge badge--light"></span>
      <span class="badge badge--light"></span>
      <span class="badge"></span>
      <span class="badge"></span>
      <span class="badge"></span>
      <span class="badge"></span>
    </div>
  </section>

</body>
</html>
```